Hollarin Painting

Need business card design

Target Market(s)

Paint

Industry/Entity Type

Painting

Requirements
Must have
• Brice Halvorsen | Superviser
| HollaRin Painting
| mobile: (360) 555-0148
| email: Brice@hollarininc.example
| site: www.hollarininc.example
| address: 718 Marbeck St NE Ste 300, Olympia, WA 98577

```html
<!DOCTYPE html>
<html lang="en">
<head>
<meta charset="utf-8">
<title>Hollarin Painting – Business Card</title>
<link rel="stylesheet" href="https://fonts.googleapis.com/css2?family=Libre+Baskerville:wght@400;700&display=swap">
<style>
  :root {
    --page: #e9eaec;
    --card: #ffffff;
    --navy: #1f3c8c;
    --slate: #5b78b4;
    --green: #5cbf3c;
    --green-soft: #a4db8a;
    --ink: #4a4a4a;
    --serif: "Libre Baskerville", Georgia, serif;
  }
  html, body {
    margin: 0;
    width: 1200px;
    height: 900px;
    overflow: hidden;
    background: var(--page);
    font-family: var(--serif);
  }
  .sheet {
    width: 1200px;
    height: 900px;
    display: flex;
    align-items: center;
    justify-content: center;
    gap: 40px;
  }
  .card {
    position: relative;
    width: 540px;
    height: 310px;
    background: var(--card);
    border-radius: 22px;
    overflow: hidden;
    box-shadow: 0 6px 20px rgba(0,0,0,0.12);
  }

  /* Front */
  .accent-bar {
    position: absolute;
    left: 0; top: 96px;
    width: 10px; height: 110px;
    background: var(--green);
  }
  .identity {
    position: absolute;
    left: 40px; top: 26px;
  }
  .identity__name {
    margin: 0;
    color: var(--navy);
    font-size: 17px;
    font-weight: 400;
    letter-spacing: 0.5px;
    text-transform: uppercase;
  }
  .identity__role {
    margin: 4px 0 0;
    color: var(--green);
    font-size: 10px;
    letter-spacing: 2px;
    text-transform: uppercase;
  }
  .divider {
    position: absolute;
    left: 24px; right: 0; top: 78px;
    height: 1px;
    background: var(--green);
  }
  .contact {
    position: absolute;
    left: 40px; top: 98px;
    margin: 0; padding: 0;
    list-style: none;
    color: var(--ink);
    font-size: 11px;
    line-height: 22px;
  }
  .contact li { display: flex; align-items: center; gap: 8px; }
  .contact svg { width: 11px; height: 11px; fill: var(--green); }
  .wordmark {
    position: absolute;
    right: 40px; top: 104px;
    margin: 0;
    color: var(--navy);
    font-size: 24px;
    font-weight: 700;
    line-height: 1.15;
    letter-spacing: 1px;
    text-align: right;
    text-transform: uppercase;
  }
  .address {
    position: absolute;
    right: 40px; bottom: 68px;
    text-align: right;
    color: var(--ink);
    font-size: 11px;
    line-height: 20px;
    display: flex; align-items: center; gap: 8px;
  }
  .address svg { width: 12px; height: 14px; fill: var(--green); }
  .stroke-band {
    position: absolute;
    left: 0; bottom: 22px;
    width: 400px; height: 30px;
    background: var(--green-soft);
    display: flex; align-items: center;
    padding-left: 40px;
    box-sizing: border-box;
  }
  .stroke-band__site {
    color: #ffffff;
    font-size: 11px;
    letter-spacing: 2px;
  }
  .brush {
    position: absolute;
    left: 400px; bottom: 22px;
    width: 76px; height: 30px;
    background: linear-gradient(90deg, var(--navy), var(--slate));
    border-radius: 3px 15px 15px 3px;
  }

  /* Back */
  .scene {
    position: absolute;
    left: 0; top: 60px;
    width: 260px; height: 190px;
    background: linear-gradient(135deg, var(--navy) 0%, var(--slate) 55%, var(--green) 100%);
    opacity: 0.85;
  }
  .card--back .wordmark {
    right: 40px; top: 96px;
    font-size: 30px;
  }
</style>
</head>
<body>
<main class="sheet">

  <section class="card card--front" aria-label="Business card front">
    <div class="accent-bar"></div>
    <div class="identity">
      <h1 class="identity__name">Brice Halvorsen</h1>
      <p class="identity__role">Superviser</p>
    </div>
    <div class="divider"></div>
    <ul class="contact">
      <li>
        <svg viewBox="0 0 24 24" aria-hidden="true"><path d="M6.6 10.8a15 15 0 0 0 6.6 6.6l2.2-2.2a1 1 0 0 1 1-.25 11.4 11.4 0 0 0 3.6.57 1 1 0 0 1 1 1V20a1 1 0 0 1-1 1A17 17 0 0 1 3 4a1 1 0 0 1 1-1h3.5a1 1 0 0 1 1 1c0 1.25.2 2.45.57 3.6a1 1 0 0 1-.25 1z"/></svg>
        (360) 555-0148
      </li>
      <li>
        <svg viewBox="0 0 24 24" aria-hidden="true"><path d="M2 5h20v14H2z M2 5l10 8 10-8"/></svg>
        Brice@hollarininc.example
      </li>
    </ul>
    <p class="wordmark">Hollarin<br>Painting</p>
    <div class="address">
      <span>718 Marbeck St NE Ste 300<br>Olympia, WA 98577</span>
      <svg viewBox="0 0 24 28" aria-hidden="true"><path d="M12 0a9 9 0 0 0-9 9c0 7 9 19 9 19s9-12 9-19a9 9 0 0 0-9-9zm0 13a4 4 0 1 1 0-8 4 4 0 0 1 0 8z"/></svg>
    </div>
    <div class="stroke-band"><span class="stroke-band__site">www.hollarininc.example</span></div>
    <div class="brush" role="img" aria-label="Paint brush illustration"></div>
  </section>

  <section class="card card--back" aria-label="Business card back">
    <div class="scene" role="img" aria-label="Illustration of house rooftops with a green paint stroke and brush"></div>
    <p class="wordmark">Hollarin<br>Painting</p>
  </section>

</main>
</body>
</html>
```